Data Flow Illustrative Diagram

We'd like an illustrative diagram for a data product we are developing. The product is based in the construction industry and is a rating system for contractros.
We want to illustrate a number of states in the process.
1. Data Collection
- We have an online interface in which contractors can upload their data in multiple formats.
- Data is also collected from third party data feeds
- All Data is stored in a centralized database
2. Data Cleansing and Merging
- The collected data from all sources is cleansed and merged together
- Need to highlight that this data is secure and never shared
3. Data Prep/Ratio Calculation
- The data is then manipulated to show and prepared for a run through a financial model
- Again, need to indicate that the orginal RAW data collected in 1 and 2 is never shared
4. Model Run / Scoring
We run financial models on the data produced in Stage 3 to generate a "score/grade" for the individual contractors
5a. Dashboard - Paying Users
The contractor "score/grade" from 4 is available on a dashboard for paying users to see
5b. Dashboard - contractors
The contractor can also log into a dashboard to see their individual score along with where they rank amongst other contractors.
6. We gather contractor project review information and feed it into the model the the Dashboard/interface
7. Machine Learning / Artificial Intelligence
- We need another component off of Stage 3/4 that indicates we are running machine learning algorithms on the data to produce constantly improving results.
This illustrative diagram will be shown to contractors as well as technical companies so it should be clear and easy to understand.
Our website/company colours are purple (accented with blue).
See the two attached diagrams for very basic ideas of the flow. We'd like something much more polished and professional but extremely easy to understand.
Extending the deadline and guaranteeing the project.
- Please note that I'm looking to show a flow of data moving through a system. Not simply an itemized list
- This is in the construction industry and should reflect that.
- IMPORTANT TO HIGHLIGHT: This is a centralized database for the industry. Data is collected from multiple sources and stored in a secure central location.
Construction Industry
Construction

```html
<!DOCTYPE html>
<html lang="en">
<head>
<meta charset="utf-8">
<title>Contractor Rating Data Flow</title>
<link href="https://fonts.googleapis.com/css2?family=Signika:wght@400;600;700&display=swap" rel="stylesheet">
<style>
:root{
  --purple:#5b2a9e;
  --purple-mid:#6a3bb8;
  --navy:#2a2480;
  --blue:#3b7bb2;
  --red:#c8161d;
  --yellow:#f5e21a;
  --orange:#e07b12;
  --magenta:#c4137f;
  --green:#4f8a1f;
  --green-light:#a6e59a;
  --ink:#1d1d2b;
  --white:#ffffff;
}
*{margin:0;padding:0;box-sizing:border-box}
html,body{width:1200px;height:927px;overflow:hidden}
body{font-family:"Signika",sans-serif;color:var(--ink)}
.canvas{position:relative;width:1200px;height:927px;overflow:hidden;
  background:linear-gradient(100deg,#ffffff 0%,#ffffff 38%,#dce9f6 60%,#8db8e0 82%,#5b9bd0 100%)}
.flow{position:absolute;left:0;top:0}
.t{position:absolute;line-height:1.15;white-space:nowrap}
.title-small{left:850px;top:30px;font-size:29px;font-weight:700;color:#eef4fb}
.title-big{left:846px;top:54px;font-size:76px;font-weight:700;color:#eef4fb;letter-spacing:-1px;line-height:1}
.label{font-size:15.5px}
.stage{position:absolute;text-align:center;color:var(--white);white-space:nowrap}
.stage .head{font-weight:600;line-height:1}
.stage .sub{font-weight:600;line-height:1.15;border-top:1.5px solid rgba(255,255,255,.85);display:inline-block;padding:1px 4px 0}
.stage .body{line-height:1.2;margin-top:2px}
.num{position:absolute;font-weight:700;text-align:center;line-height:1}
.visit{left:56px;top:822px;font-size:16px;color:#333}
.socials{position:absolute;left:52px;top:860px;display:flex;gap:10px;font-size:11px;color:var(--navy);font-weight:600}
.socials span{display:flex;align-items:center;gap:3px}
.socials i{display:inline-block;width:12px;height:12px;border-radius:50%;background:var(--navy)}
.know{left:880px;top:838px;font-size:16px;color:#222}
.url{left:880px;top:858px;font-size:24px;color:var(--navy);letter-spacing:.5px}
.spanish{left:944px;top:518px;width:200px;text-align:center;font-size:16px;white-space:normal}
.secure-note{left:768px;top:368px;font-size:16px}
</style>
</head>
<body>
<main class="canvas">
<svg class="flow" width="1200" height="927" viewBox="0 0 1200 927">
  <defs>
    <symbol id="lock" viewBox="0 0 28 28">
      <circle cx="14" cy="14" r="13" fill="var(--navy)" stroke="#fff" stroke-width="1.5"/>
      <rect x="8.5" y="12.5" width="11" height="8.5" rx="1" fill="#fff"/>
      <path d="M10.5 12.5v-2.5a3.5 3.5 0 0 1 7 0v2.5" fill="none" stroke="#fff" stroke-width="1.8"/>
    </symbol>
    <symbol id="shield" viewBox="0 0 30 34">
      <path d="M15 1 L29 6 V16 C29 25 22 31 15 33 C8 31 1 25 1 16 V6 Z" fill="#6a3bb8" stroke="#fff" stroke-width="1.5"/>
      <text x="15" y="18" font-size="5.5" text-anchor="middle" fill="#fff" font-family="Signika,sans-serif">security</text>
    </symbol>
    <path id="arcTop" d="M484 224 A140 140 0 0 1 664 140"/>
    <path id="arcBottom" d="M533 382 A138 138 0 0 0 751 298"/>
  </defs>

  <g fill="none" stroke="#444" stroke-width="1.6" stroke-dasharray="2 3">
    <path d="M298 190 V200 H416 L474 234"/>
    <path d="M320 292 V332 H440 L480 286"/>
    <path d="M312 387 H452 L494 326"/>
    <path d="M170 442 H444 L520 358"/>
    <path d="M724 272 H746"/>
    <path d="M888 272 H908"/>
    <path d="M972 484 L920 536 V588"/>
    <path d="M744 568 H792 L846 600"/>
    <path d="M734 810 H784 L840 774"/>
    <path d="M540 806 H504 L488 772"/>
    <path d="M464 608 L504 564 H556"/>
  </g>
  <path d="M960 272 H980 L1012 356" fill="none" stroke="#222" stroke-width="1.4"/>

  <!-- central database hub -->
  <circle cx="616" cy="272" r="118" fill="none" stroke="var(--green)" stroke-width="5" stroke-dasharray="250 70 290 132"/>
  <circle cx="616" cy="272" r="108" fill="var(--green-light)"/>
  <circle cx="616" cy="272" r="60" fill="#fff"/>
  <g role="img" aria-label="Construction workers around a cloud server holding the central database">
    <ellipse cx="616" cy="256" rx="46" ry="26" fill="#8a6fd0"/>
    <rect x="594" y="228" width="44" height="44" rx="3" fill="#3a3a4a"/>
    <circle cx="616" cy="182" r="14" fill="#7aa7d8"/>
    <circle cx="547" cy="218" r="14" fill="#7aa7d8"/>
    <circle cx="685" cy="218" r="14" fill="#7aa7d8"/>
    <circle cx="545" cy="292" r="14" fill="#e0b060"/>
    <circle cx="687" cy="292" r="14" fill="#e0b060"/>
    <circle cx="616" cy="336" r="14" fill="#e08a50"/>
  </g>
  <text font-size="14" fill="var(--ink)" font-family="Signika,sans-serif"><textPath href="#arcTop">Your data is always protected</textPath></text>
  <text font-size="14.5" fill="var(--ink)" font-family="Signika,sans-serif"><textPath href="#arcBottom">All information goes to a central computer</textPath></text>
  <use href="#shield" x="662" y="128" width="32" height="38"/>
  <use href="#lock" x="474" y="226" width="28" height="28"/>
  <use href="#lock" x="476" y="262" width="28" height="28"/>
  <use href="#lock" x="488" y="302" width="28" height="28"/>
  <use href="#lock" x="514" y="336" width="28" height="28"/>

  <rect x="254" y="112" width="82" height="60" rx="4" fill="#6fa0d8" role="img" aria-label="Computer monitor showing an online registration page"/>
  <rect x="280" y="172" width="30" height="16" fill="#b8c4d4"/>
  <rect x="272" y="216" width="80" height="76" fill="#eef0f4" stroke="#c8ccd6" role="img" aria-label="Paper registration form with a worker profile"/>
  <rect x="204" y="304" width="106" height="84" rx="8" fill="#7d9bd0" role="img" aria-label="Hands holding a tablet running the app"/>
  <rect x="58" y="344" width="90" height="58" rx="3" fill="#cfe0f4" stroke="#9ab" role="img" aria-label="Third party personal data record card"/>

  <!-- stage 1 -->
  <circle cx="166" cy="212" r="66" fill="none" stroke="#4f6fc0" stroke-width="3" stroke-dasharray="300 115"/>
  <circle cx="166" cy="212" r="58" fill="var(--purple)"/>
  <circle cx="90" cy="206" r="24" fill="#fff" stroke="#3b5fb0" stroke-width="4"/>

  <!-- stage 2 -->
  <circle cx="836" cy="276" r="62" fill="var(--yellow)" stroke="#fff" stroke-width="3"/>
  <circle cx="768" cy="270" r="22" fill="#fff" stroke="var(--yellow)" stroke-width="4"/>
  <use href="#lock" x="852" y="214" width="24" height="24"/>
  <use href="#shield" x="840" y="312" width="24" height="28"/>
  <rect x="908" y="182" width="50" height="182" rx="3" fill="#dfe6f5" stroke="#8a9ad0" stroke-width="2" role="img" aria-label="Column of three registered contractors"/>

  <rect x="1020" y="244" width="120" height="120" rx="6" fill="#c9d6ee" role="img" aria-label="Financial documents, cash and a pen"/>

  <!-- stage 3 -->
  <circle cx="1052" cy="432" r="82" fill="none" stroke="var(--red)" stroke-width="3" stroke-dasharray="360 155"/>
  <circle cx="1052" cy="432" r="76" fill="var(--red)"/>
  <circle cx="958" cy="424" r="30" fill="#fff" stroke="var(--red)" stroke-width="4"/>
  <use href="#lock" x="1120" y="402" width="26" height="26"/>
  <use href="#shield" x="1118" y="442" width="28" height="32"/>

  <!-- stage 4 -->
  <circle cx="904" cy="688" r="108" fill="none" stroke="var(--blue)" stroke-width="3" stroke-dasharray="470 209"/>
  <circle cx="904" cy="688" r="100" fill="var(--blue)"/>
  <circle cx="794" cy="680" r="36" fill="#fff" stroke="var(--blue)" stroke-width="5"/>
  <use href="#lock" x="986" y="640" width="28" height="28"/>
  <use href="#shield" x="986" y="682" width="30" height="34"/>

  <!-- stage 5a -->
  <rect x="400" y="460" width="140" height="100" rx="6" fill="#e4e8ef" role="img" aria-label="Three construction workers in work clothes"/>
  <rect x="760" y="466" width="120" height="94" rx="6" fill="#e4e8ef" role="img" aria-label="Three construction workers in work clothes"/>
  <circle cx="664" cy="540" r="88" fill="none" stroke="var(--purple)" stroke-width="3" stroke-dasharray="400 153"/>
  <circle cx="664" cy="540" r="80" fill="var(--purple-mid)"/>
  <circle cx="570" cy="534" r="32" fill="#fff" stroke="var(--purple)" stroke-width="5"/>
  <use href="#lock" x="732" y="504" width="22" height="22"/>
  <use href="#shield" x="730" y="540" width="24" height="28"/>

  <!-- stage 5b -->
  <circle cx="658" cy="812" r="84" fill="none" stroke="var(--red)" stroke-width="3" stroke-dasharray="380 148"/>
  <circle cx="658" cy="812" r="76" fill="var(--red)"/>
  <rect x="636" y="676" width="44" height="66" rx="6" fill="#8a94a8" role="img" aria-label="Contractor wearing a hard hat"/>
  <circle cx="574" cy="796" r="32" fill="#fff" stroke="var(--red)" stroke-width="5"/>
  <use href="#lock" x="730" y="764" width="22" height="22"/>
  <use href="#shield" x="728" y="800" width="24" height="28"/>

  <!-- stage 6 -->
  <circle cx="436" cy="688" r="88" fill="none" stroke="var(--yellow)" stroke-width="4" stroke-dasharray="400 153"/>
  <circle cx="436" cy="688" r="80" fill="var(--orange)"/>
  <circle cx="352" cy="682" r="30" fill="#fff" stroke="var(--yellow)" stroke-width="5"/>
  <path d="M500 652 L514 674 L552 606" fill="none" stroke="var(--orange)" stroke-width="4"/>
  <use href="#lock" x="516" y="676" width="22" height="22"/>
  <use href="#shield" x="514" y="712" width="24" height="28"/>

  <!-- stage 7 -->
  <circle cx="216" cy="580" r="114" fill="none" stroke="var(--magenta)" stroke-width="4" stroke-dasharray="510 206"/>
  <circle cx="216" cy="580" r="104" fill="var(--magenta)"/>
  <circle cx="216" cy="580" r="96" fill="none" stroke="#fff" stroke-width="2"/>
  <circle cx="98" cy="572" r="38" fill="#fff" stroke="var(--magenta)" stroke-width="5"/>
  <use href="#lock" x="316" y="536" width="30" height="30"/>
  <use href="#shield" x="314" y="584" width="30" height="34"/>
</svg>

<div class="t title-small">Illustrative</div>
<div class="t title-big">Diagram</div>

<div class="t label" style="left:352px;top:114px">Enter our site<br>and use our online<br>registration</div>
<div class="t label" style="left:365px;top:242px">Fill out<br>the forms</div>
<div class="t label" style="left:216px;top:402px">Use our App</div>
<div class="t label" style="left:59px;top:406px">We also process<br>third party data</div>
<div class="t secure-note">This data is secure<br>and never shared</div>
<div class="t spanish">Los datos RAW originales recogidos en 1 y 2 nunca se comparten</div>

<div class="num" style="left:72px;top:186px;width:36px;font-size:40px;color:var(--purple)">1</div>
<div class="stage" style="left:112px;top:170px;width:108px">
  <div class="head" style="font-size:30px">•DATA</div>
  <div class="sub" style="font-size:14px">COLLECTION</div>
  <div class="body" style="font-size:9.5px">Use the different media<br>at your disposal and<br>charge your data</div>
</div>

<div class="num" style="left:752px;top:252px;width:32px;font-size:34px;color:var(--yellow)">2</div>
<div class="stage" style="left:786px;top:240px;width:104px;color:var(--ink)">
  <div class="head" style="font-size:27px">•Filter</div>
  <div class="sub" style="font-size:12.5px;border-color:var(--ink)">Registered Data</div>
  <div class="body" style="font-size:8px">The collected data from<br>all sources is cleansed and<br>merged together</div>
</div>

<div class="num" style="left:936px;top:398px;width:44px;font-size:50px;color:var(--red)">3</div>
<div class="stage" style="left:980px;top:378px;width:148px">
  <div class="body" style="font-size:12px;font-weight:600;margin:0">Preparation of</div>
  <div class="head" style="font-size:35px">•Data</div>
  <div class="sub" style="font-size:16px">Calculation Ratio</div>
  <div class="body" style="font-size:9.5px">The data is then manipulated<br>to show and prepared for<br>a run through a financial<br>model</div>
</div>

<div class="num" style="left:768px;top:648px;width:52px;font-size:60px;color:var(--blue)">4</div>
<div class="stage" style="left:812px;top:640px;width:188px">
  <div class="head" style="font-size:27px">•Model Run</div>
  <div class="sub" style="font-size:21px">Scoring</div>
  <div class="body" style="font-size:11px">We run financial models<br>on the data produced in Stage 3<br>to generate a "score/grade"<br>for the individual<br>contractors</div>
</div>

<div class="num" style="left:540px;top:510px;width:62px;font-size:46px;color:var(--purple)">5<span style="font-size:28px">a</span></div>
<div class="stage" style="left:596px;top:506px;width:136px">
  <div class="head" style="font-size:20px">•Paying Users</div>
  <div class="sub" style="font-size:17px">Dashboard</div>
  <div class="body" style="font-size:9.5px">The contractor "score/grade"<br>from 4 is available on a<br>dashboard for paying<br>users to see</div>
</div>

<div class="num" style="left:544px;top:772px;width:62px;font-size:46px;color:var(--red)">5<span style="font-size:28px">b</span></div>
<div class="stage" style="left:590px;top:762px;width:140px">
  <div class="head" style="font-size:20px">•Contractors</div>
  <div class="sub" style="font-size:17px">Dashboard</div>
  <div class="body" style="font-size:9px">We run financial models<br>on the data produced in Stage 3<br>to generate a "score/grade"<br>for the individual<br>contractors</div>
</div>

<div class="num" style="left:330px;top:658px;width:44px;font-size:46px;color:var(--yellow)">6</div>
<div class="stage" style="left:376px;top:638px;width:128px">
  <div class="head" style="font-size:28px">•Review</div>
  <div class="sub" style="font-size:16px">information</div>
  <div class="body" style="font-size:9.5px">We gather contractor project<br>review information and<br>feed it into the model the<br>Dashboard/interface</div>
</div>

<div class="num" style="left:70px;top:538px;width:56px;font-size:66px;color:var(--magenta)">7</div>
<div class="stage" style="left:130px;top:500px;width:182px">
  <div class="head" style="font-size:31px">•Machine<br>Learning</div>
  <div class="sub" style="font-size:17.5px">Artificial Intelligence</div>
  <div class="body" style="font-size:12px">We are running machine<br>learning algorithms on the data<br>to produce constantly<br>improving results.</div>
</div>

<div class="t visit">Visit us on:</div>
<div class="socials">
  <span><i></i>Crewline</span>
  <span><i></i>Sitecast</span>
  <span><i></i>Tubeyard</span>
  <span><i></i>Chatpost</span>
  <span><i></i>Snapframe</span>
</div>
<div class="t know">Know more on:</div>
<div class="t url">www.crewscore.example</div>
</main>
</body>
</html>
```